Quillbrook Health needs a new services brochure

We need a new brochure that highlights the services that we offer at our clinic. We are a multidisciplinary health clinic that focuses on injury rehabilitation and pain management. We are looking for a brochure that will highlight our primary services to our clientele and inform potential clients of what we can offer. We pride ourselves on our quality of care and our advanced treatment techniques.
Target Market(s)
young families, athletes, people interested in their health.
Industry/Entity Type
Health And Wellness
Colors
Designer to choose colors to be used in the design.
Requirements
Must have
- We would love our new brochure to be a tri-fold that has 6 pages. We would like it to have brief information about our featured services:
- - Chiropractic
- - Massage Therapy
- - Manual Osteopathic Therapy
- - Acupuncture
- - Laser Therapy
- - Radial Shockwave Therapy
- We would also like this brochure to include a brief price list and direct billing info, About Us section & Contact information.
Nice to have
- If there is space to list that we also offer other services such as : Tissue Unwind Method, Hot Stone Massage, Cupping Technique, Pembrill Method, and Kinesiology Taping that would be great. We would like to use images similar to those that are on our website (we have hi-res of all images on the website) www.quillbrookhealth.ca and colours that would fit with our logo.

```html
<!DOCTYPE html>
<html lang="en">
<head>
<meta charset="utf-8">
<title>Quillbrook Health – Services Brochure</title>
<link href="https://fonts.googleapis.com/css2?family=Oswald:wght@400;500;600&family=Open+Sans:wght@400;600;700&display=swap" rel="stylesheet">
<style>
  :root{
    --blue:#1b6db3;
    --blue-dark:#0f4d87;
    --blue-light:#4a93d1;
    --grey-bg:#d9dadc;
    --grey-band:#6d6f73;
    --ink:#3b3d40;
    --white:#ffffff;
    --paper:#f7f8f9;
  }
  *{box-sizing:border-box;margin:0;padding:0}
  html,body{width:796px;height:1200px;overflow:hidden;background:var(--grey-bg)}
  body{font-family:"Open Sans",Arial,sans-serif;color:var(--ink);position:relative}
  h2,h3,.display{font-family:"Oswald","Arial Narrow",sans-serif;font-weight:500}
  .sheet{position:absolute;left:20px;width:756px;height:560px;display:flex;background:var(--paper);box-shadow:0 4px 14px rgba(0,0,0,.25)}
  .sheet--outside{top:30px}
  .sheet--inside{top:610px}
  .panel{position:relative;width:252px;height:560px;overflow:hidden}
  .panel + .panel{border-left:1px solid rgba(0,0,0,.08)}
  .photo{position:absolute;display:block}

  /* Outside – about */
  .about .photo{left:0;top:0;width:252px;height:160px;background:linear-gradient(180deg,#8fc2ea 0%,#cfe5f6 70%,#e9c9a9 100%)}
  .about__body{position:absolute;top:172px;left:18px;right:18px}
  .about__title{color:var(--blue);font-size:20px;margin-bottom:6px}
  .about p{font-size:9.5px;line-height:1.55}
  .about__why{position:absolute;left:0;bottom:0;width:252px;height:200px;color:var(--white)}
  .about__why svg{position:absolute;top:0;left:0}
  .about__why .why-text{position:absolute;top:54px;left:18px;right:18px;z-index:1}
  .why-title{color:var(--white);font-size:17px;margin-bottom:6px}

  /* Outside – contact */
  .contact__top{position:absolute;top:0;left:0;width:252px;height:250px;background:var(--blue);color:var(--white);padding:16px 20px}
  .contact h3{font-size:14px;letter-spacing:.5px;text-align:center;margin-bottom:6px;text-transform:uppercase}
  .hours{width:100%;font-size:9px;border-collapse:collapse;margin-bottom:12px}
  .hours td{padding:2px 0;border-bottom:1px solid rgba(255,255,255,.3)}
  .hours td:last-child{text-align:right}
  .contact address{font-style:normal;font-size:9.5px;line-height:1.6;text-align:center}
  .contact__phone{position:absolute;top:262px;left:0;width:252px;text-align:center;font-family:"Oswald",sans-serif;font-size:20px;color:var(--blue-dark);font-weight:500}
  .contact__ring{position:absolute;top:296px;left:46px;width:160px;height:160px;border-radius:50%;background:var(--grey-band)}
  .contact .photo{top:306px;left:56px;width:140px;height:140px;border-radius:50%;background:radial-gradient(circle at 50% 45%,#d8a58a 0%,#a86f55 55%,#3a3f48 100%)}
  .contact__band{position:absolute;left:0;bottom:0;width:252px;height:60px;background:var(--grey-band)}

  /* Outside – cover */
  .cover__brand{position:absolute;top:18px;left:0;width:252px;text-align:center}
  .brand{display:inline-flex;align-items:center;gap:8px;font-family:"Oswald",sans-serif;font-weight:500;font-size:20px;color:var(--blue)}
  .brand__dot{width:16px;height:16px;border-radius:50%;background:var(--blue)}
  .cover__tag{font-size:9px;color:var(--ink);margin-top:2px}
  .cover .photo{left:0;top:80px;width:252px;height:320px;background:linear-gradient(180deg,#bcd9ef 0%,#9cc6e6 45%,#3c79b8 100%)}
  .cover__band{position:absolute;left:0;bottom:0;width:252px;height:200px}
  .cover__band svg{position:absolute;top:0;left:0}
  .cover__title{position:absolute;left:0;bottom:40px;width:252px;text-align:center;color:var(--white);font-family:"Oswald",sans-serif;line-height:1}
  .cover__title span{display:block;font-size:22px;letter-spacing:2px}
  .cover__title strong{display:block;font-size:46px;font-weight:600;letter-spacing:3px;margin:2px 0}

  /* Inside – services intro */
  .intro .photo{left:0;top:0;width:252px;height:230px;background:linear-gradient(160deg,#6b4a3a 0%,#b7876c 50%,#3b2c26 100%)}
  .intro__wave{position:absolute;left:0;top:150px;z-index:1}
  .intro__label{position:absolute;top:212px;right:14px;z-index:2;color:var(--white);font-family:"Oswald",sans-serif;font-size:11.5px;line-height:14px}
  .intro__body{position:absolute;top:250px;left:18px;right:18px}
  .intro h2{font-size:26px;color:var(--blue);margin-bottom:8px}
  .intro p{font-size:9.5px;line-height:1.6;margin-bottom:10px}
  .intro__extra{font-weight:600;color:var(--blue-dark)}

  /* Inside – service list */
  .service-list{background:var(--blue);padding:18px 16px;display:flex;flex-direction:column;gap:10px}
  .service{display:flex;align-items:center;gap:10px;height:78px}
  .service--flip{flex-direction:row-reverse;text-align:right}
  .service .photo{position:static;width:92px;height:78px;flex:none;border:2px solid var(--white);background:linear-gradient(135deg,#d2b39e,#8e6a57)}
  .service h3{color:var(--white);font-size:13px;line-height:1.2;flex:1}

  /* Inside – prices */
  .prices{padding:18px 18px}
  .prices h2{font-size:20px;color:var(--blue);margin-bottom:8px}
  .price-group{margin-bottom:9px}
  .price-group h3{font-size:11px;color:var(--white);background:var(--blue);padding:2px 8px;margin-bottom:3px}
  .price-row{display:flex;justify-content:space-between;font-size:9px;padding:2px 8px;border-bottom:1px dotted #b9bcc0}
  .billing h3{font-size:13px;color:var(--blue-dark);margin:6px 0 3px}
  .billing p{font-size:9px;line-height:1.5}
  .prices__web{position:absolute;left:0;bottom:0;width:252px;height:34px;background:var(--blue);color:var(--white);font-size:10px;font-weight:600;text-align:center;line-height:34px}
</style>
</head>
<body>

<section class="sheet sheet--outside">
  <div class="panel about">
    <div class="photo" role="img" aria-label="Photo of a woman leaping joyfully against a bright blue sky"></div>
    <div class="about__body">
      <h2 class="about__title">About Us</h2>
      <p>Quillbrook Health is a multidisciplinary clinic focused on injury rehabilitation and pain management. Our team of practitioners works together to build a care plan around your goals, helping you move better, recover faster and stay active with your family.</p>
    </div>
    <div class="about__why">
      <svg width="252" height="200" viewBox="0 0 252 200" aria-hidden="true">
        <path d="M0 40 Q126 0 252 30 L252 200 L0 200Z" fill="var(--blue)"/>
        <path d="M0 40 Q126 0 252 30" fill="none" stroke="var(--blue-light)" stroke-width="4"/>
      </svg>
      <div class="why-text">
        <h2 class="why-title">Why Quillbrook Health?</h2>
        <p>We pride ourselves on quality of care and advanced treatment techniques. Every visit is one-on-one, every plan is personal, and our clinic directly bills most insurance providers.</p>
      </div>
    </div>
  </div>

  <div class="panel contact">
    <div class="contact__top">
      <h3>Opening Hours</h3>
      <table class="hours">
        <tr><td>Monday – Friday</td><td>8:00am – 8:00pm</td></tr>
        <tr><td>Saturday</td><td>9:00am – 4:00pm</td></tr>
        <tr><td>Sunday</td><td>Closed</td></tr>
      </table>
      <h3>Get in Touch</h3>
      <address>214 Larkspur Avenue NW<br>Calgary, AB T2P 0K4<br>info@quillbrookhealth.ca</address>
    </div>
    <div class="contact__phone">(403) 555-0187</div>
    <div class="contact__ring"></div>
    <div class="photo" role="img" aria-label="Photo of a therapist treating a patient's upper back"></div>
    <div class="contact__band"></div>
  </div>

  <div class="panel cover">
    <div class="cover__brand">
      <div class="brand"><span class="brand__dot"></span>Quillbrook Health</div>
      <div class="cover__tag">live life pain free</div>
    </div>
    <div class="photo" role="img" aria-label="Photo of a smiling woman stretching outdoors by the sea"></div>
    <div class="cover__band">
      <svg width="252" height="200" viewBox="0 0 252 200" aria-hidden="true">
        <path d="M0 50 Q140 10 252 0 L252 200 L0 200Z" fill="var(--blue)"/>
        <path d="M0 50 Q140 10 252 0" fill="none" stroke="var(--white)" stroke-width="4"/>
      </svg>
      <div class="cover__title"><span>A BETTER</span><strong>LIFE</strong><span>EVERYDAY</span></div>
    </div>
  </div>
</section>

<section class="sheet sheet--inside">
  <div class="panel intro">
    <div class="photo" role="img" aria-label="Photo of a hot stone massage on a client's back"></div>
    <svg class="intro__wave" width="252" height="80" viewBox="0 0 252 80" aria-hidden="true">
      <path d="M0 80 L0 55 Q120 65 252 0 L252 80Z" fill="var(--paper)"/>
      <path d="M60 80 Q170 60 252 14 L252 80Z" fill="var(--blue)"/>
    </svg>
    <div class="intro__label">Hot Stone Massage</div>
    <div class="intro__body">
      <h2>Services</h2>
      <p>From sports injuries to everyday aches, our practitioners combine hands-on care with modern therapies to reduce pain and restore movement.</p>
      <p class="intro__extra">We also offer Tissue Unwind Method, Hot Stone Massage, Cupping Technique, Pembrill Method and Kinesiology Taping.</p>
    </div>
  </div>

  <div class="panel service-list">
    <div class="service"><div class="photo" role="img" aria-label="Photo of a chiropractic adjustment"></div><h3>Chiropractic</h3></div>
    <div class="service service--flip"><div class="photo" role="img" aria-label="Photo of a massage therapy session"></div><h3>Massage Therapy</h3></div>
    <div class="service"><div class="photo" role="img" aria-label="Photo of manual osteopathic therapy"></div><h3>Manual Osteopathic Therapy</h3></div>
    <div class="service service--flip"><div class="photo" role="img" aria-label="Photo of acupuncture needles on a back"></div><h3>Acupuncture</h3></div>
    <div class="service"><div class="photo" role="img" aria-label="Photo of laser therapy on a knee"></div><h3>Laser Therapy</h3></div>
    <div class="service service--flip"><div class="photo" role="img" aria-label="Photo of radial shockwave therapy on a shoulder"></div><h3>Radial Shockwave Therapy</h3></div>
  </div>

  <div class="panel prices">
    <h2>Price List</h2>
    <div class="price-group"><h3>Chiropractic</h3>
      <div class="price-row"><span>Initial Assessment</span><span>$85</span></div>
      <div class="price-row"><span>Treatment</span><span>$55</span></div></div>
    <div class="price-group"><h3>Massage Therapy</h3>
      <div class="price-row"><span>30 Minutes</span><span>$60</span></div>
      <div class="price-row"><span>60 Minutes</span><span>$95</span></div></div>
    <div class="price-group"><h3>Acupuncture</h3>
      <div class="price-row"><span>Initial Visit</span><span>$90</span></div>
      <div class="price-row"><span>Follow-up</span><span>$70</span></div></div>
    <div class="price-group"><h3>Laser Therapy</h3>
      <div class="price-row"><span>Per Session</span><span>$50</span></div></div>
    <div class="price-group"><h3>Shockwave Therapy</h3>
      <div class="price-row"><span>Per Session</span><span>$75</span></div></div>
    <div class="billing">
      <h3>Direct Billing</h3>
      <p>We bill most extended health plans directly, so you pay only what is not covered.</p>
    </div>
    <div class="prices__web">www.quillbrookhealth.ca</div>
  </div>
</section>

</body>
</html>
```